Ferncrest Dental, LLC business card project

Business card to be designed with current logo.
Dental office- please keep design of card that looks clean and professional.
Please include the following info:
Ferncrest Dental, LLC
Dr. Lorna Pettigrew
2871 Marlowe Street
Bethlehem, PA 18093
610-555-0193
ferncrestdental.office@examplemail.test
Hello everyone-
Reason: Just got back from overseas- will look at all designs and provide feedback. Thank you!
Reason: Polling my friends for the final selection-
thank you to all those that participated- so many talented designers!

```html
<!DOCTYPE html>
<html lang="en">
<head>
<meta charset="utf-8">
<title>Ferncrest Dental, LLC — Business Card</title>
<link rel="stylesheet" href="https://fonts.googleapis.com/css2?family=Arimo:wght@700&family=Questrial&display=swap">
<style>
  :root {
    --page: #ffffff;
    --card-face: #efedf0;
    --lilac: #c49cc8;
    --brand-green: #6aa843;
    --ink: #231f20;
  }
  * { margin: 0; padding: 0; box-sizing: border-box; }
  html, body {
    width: 1200px;
    height: 848px;
    overflow: hidden;
    background: var(--page);
  }
  .business-card {
    position: absolute;
    left: 73px;
    top: 82px;
    width: 1003px;
    height: 649px;
    background: var(--card-face);
  }
  .brand-header {
    position: absolute;
    left: 0;
    top: 0;
    width: 100%;
    height: 176px;
    display: flex;
    align-items: center;
    justify-content: center;
    border-bottom: 4px solid var(--lilac);
  }
  .brand-name {
    font-family: "Questrial", sans-serif;
    font-size: 66px;
    color: var(--brand-green);
    letter-spacing: -0.5px;
    line-height: 1;
    padding-top: 8px;
  }
  .doctor-name {
    position: absolute;
    left: 0;
    top: 268px;
    width: 100%;
    text-align: center;
    font-family: "Arimo", sans-serif;
    font-weight: 700;
    font-size: 92px;
    letter-spacing: -3px;
    color: var(--ink);
    line-height: 1;
  }
  .contact-band {
    position: absolute;
    left: 0;
    bottom: 0;
    width: 100%;
    height: 176px;
    background: var(--lilac);
    display: flex;
    flex-direction: column;
    align-items: center;
    justify-content: center;
    font-style: normal;
  }
  .contact-line {
    font-family: "Questrial", sans-serif;
    font-size: 25px;
    letter-spacing: 1.6px;
    line-height: 35px;
    color: var(--ink);
  }
</style>
</head>
<body>
  <main class="business-card">
    <header class="brand-header">
      <h1 class="brand-name">Ferncrest Dental, LLC</h1>
    </header>

    <p class="doctor-name">Dr. Lorna Pettigrew</p>

    <address class="contact-band">
      <span class="contact-line">2871 Marlowe Street</span>
      <span class="contact-line">Bethlehem, PA 18093</span>
      <span class="contact-line">610-555-0193</span>
      <span class="contact-line">ferncrestdental.office@examplemail.test</span>
    </address>
  </main>
</body>
</html>
```